Computer consultant business card

Brimlo Software is a newly started computer consulting company. It's a small one-man company that provides mostly Velunix applications but also websites in collaboration with designers. I'm running this company on the side of full time university studies.

I want the final design to be clean and memorable. Be creative! :)

Some inspiration:
http://www.tavelpix.net/design/73519
http://www.tavelpix.net/design/2739566/business-card-design-by-quillbop
http://www.tavelpix.net/design/804613/business-card-design-by-lorvena-brukwaldsen

See attachment for my company logo.
Updates

I would like to thank everyone for submitting! I'll need a couple of days to review and ultimately select a design.

Target Market(s)

Non-technical entrepreneurs and small companies.

Industry/Entity Type

University

Requirements
Must have
• My company logo.
In any way, both colors from my logo.
First- and last name, e-mail and phone number.
Double-sided design.
Nice to have
• Something creative with the symbol in my logo

```html
<!DOCTYPE html>
<html lang="en">
<head>
<meta charset="utf-8">
<title>Brimlo Software – Business Card</title>
<link rel="stylesheet" href="https://fonts.googleapis.com/css2?family=Exo+2:wght@400;500&display=swap">
<style>
  :root {
    --stage: #2a2a2a;
    --card-dark-start: #232323;
    --card-dark-end: #0f0f0f;
    --card-light: #ffffff;
    --brand-blue: #2a7de1;
    --ink-dark: #2e2e2e;
    --ink-light: #ffffff;
  }
  * { margin: 0; padding: 0; box-sizing: border-box; }
  html, body {
    width: 1200px;
    height: 900px;
    overflow: hidden;
    background: var(--stage);
    font-family: "Exo 2", sans-serif;
  }
  .stage {
    position: relative;
    width: 1200px;
    height: 900px;
  }
  .card {
    position: absolute;
    top: 305px;
    width: 520px;
    height: 290px;
    overflow: hidden;
  }
  .card--front {
    left: 70px;
    background:
      radial-gradient(circle at 32% 55%, rgba(42,125,225,0.10) 0, rgba(42,125,225,0) 55%),
      linear-gradient(135deg, var(--card-dark-start), var(--card-dark-end));
  }
  .card--back {
    left: 615px;
    background: var(--card-light);
  }
  .brand {
    position: absolute;
    display: flex;
    align-items: center;
    font-weight: 500;
    letter-spacing: 1px;
  }
  .brand__dot {
    border-radius: 50%;
    background: var(--brand-blue);
    flex: none;
  }
  .card--front .brand {
    left: 90px;
    top: 88px;
    gap: 26px;
    color: var(--ink-light);
    font-size: 76px;
    line-height: 1;
  }
  .card--front .brand__dot { width: 108px; height: 108px; }
  .card--back .brand {
    right: 30px;
    top: 30px;
    gap: 16px;
    color: var(--ink-dark);
    font-size: 46px;
    line-height: 1;
  }
  .card--back .brand__dot { width: 70px; height: 70px; }
  .holder {
    position: absolute;
    left: 165px;
    top: 222px;
    font-size: 23px;
    font-weight: 400;
    color: var(--ink-dark);
  }
  .contact {
    position: absolute;
    left: 370px;
    top: 226px;
    list-style: none;
    font-size: 15px;
    color: var(--ink-dark);
    line-height: 20px;
  }
  .contact__item { display: flex; align-items: center; gap: 5px; }
  .contact__icon { width: 11px; height: 11px; fill: var(--brand-blue); flex: none; }
</style>
</head>
<body>
<main class="stage">
  <section class="card card--front" aria-label="Card front">
    <div class="brand"><span class="brand__dot"></span><span class="brand__name">brimlo</span></div>
  </section>

  <section class="card card--back" aria-label="Card back">
    <div class="brand"><span class="brand__dot"></span><span class="brand__name">brimlo</span></div>
    <p class="holder">Tomas Verlund</p>
    <ul class="contact">
      <li class="contact__item">
        <svg class="contact__icon" viewBox="0 0 12 12" aria-hidden="true"><path d="M2.4 0.8 4.2 2.8 3.2 4.2C3.9 5.8 5.2 7.2 6.8 8L8.2 7 10.6 8.8 9.6 11C5 11 1 7 1 2.2Z"/></svg>
        <span>5550 123 456</span>
      </li>
      <li class="contact__item">
        <svg class="contact__icon" viewBox="0 0 12 12" aria-hidden="true"><path d="M0.5 2.5H11.5V3L6 6.6 0.5 3Z M0.5 4.2 6 7.8 11.5 4.2V9.5H0.5Z"/></svg>
        <span>info@brimlo.net</span>
      </li>
    </ul>
  </section>
</main>
</body>
</html>
```